My new Bible based podcast needs a Podcast Cover Design for Vexora directory

I need a Podcast Cover Design design for my podcast listing in Vexora. The podcast is called Morning Lanterns Over Hills. I would like something cheerful, warm, and fresh because I take a non-traditional approach to explaining how the Bible is relevant to people today. My goal is to get back to the original spirituality of the Bible without all the centuries of added man-made doctrines. It would be great to show a sense of peace and hope, with new possibilities. This is not like a floating corporate logo. I need it to be square and full color/design all the way to the edges.

I have resubmitted this project because I did not understand how to ask for a podcast cover design. If you already submitted for me, I apologize for not knowing how the system works. I did not give the best picture of what I needed.

Target Market(s)

People who want a fresh look at the Bible

Industry/Entity Type

Religious

Logo Text

Morning Lanterns Over Hills

Colors

Designer to choose colors to be used in the design.

Requirements
Must have
• It must be square. The design should fill the space. See screen shot below of podcast cover designs on the Christianity/Spirituality page of Vexora directory so you can see where the podcast cover design needs to fit in and stand out.
• The final design will need to be:
• 3,000 x 3,000 pixels (but readable at 150 x 150)
• 72 dpi
• .jpg or .png format
• rgb color space
Nice to have
• Perhaps an open book suggesting the Bible, but not necessary.
Should not have
• No microphones or airwaves.

```html
<!DOCTYPE html>
<html lang="en">
<head>
<meta charset="utf-8">
<title>Morning Lanterns Over Hills — Podcast Cover</title>
<link rel="stylesheet" href="https://fonts.googleapis.com/css2?family=Playfair+Display:wght@900&family=Kaushan+Script&display=swap">
<style>
  :root {
    --teal: #78bfb3;
    --forest: #3d625a;
    --white: #ffffff;
  }
  html, body {
    margin: 0;
    padding: 0;
    width: 1200px;
    height: 1200px;
    overflow: hidden;
    background: var(--teal);
  }
  .cover {
    display: block;
    width: 1200px;
    height: 1200px;
    background: var(--teal);
  }
  .frame-line {
    stroke: var(--forest);
    stroke-width: 6;
    stroke-linecap: round;
    fill: none;
  }
  .title-word {
    font-family: "Playfair Display", Georgia, serif;
    font-weight: 900;
    fill: var(--white);
  }
  .title-accent {
    font-family: "Kaushan Script", cursive;
    fill: var(--forest);
  }
</style>
</head>
<body>
<svg class="cover" viewBox="0 0 1200 1200" xmlns="http://www.w3.org/2000/svg" role="img" aria-label="Morning Lanterns Over Hills podcast cover">
  <g class="frame">
    <path class="frame-line" d="M0 56 L300 54 L620 57 L900 55 L1200 56"/>
    <path class="frame-line" d="M0 1136 L280 1134 L640 1137 L950 1135 L1200 1136"/>
    <path class="frame-line" d="M60 0 L58 300 L62 620 L59 900 L61 1200"/>
    <path class="frame-line" d="M1146 0 L1144 320 L1148 640 L1145 920 L1147 1200"/>
  </g>

  <g class="title">
    <text class="title-word" x="600" y="360" text-anchor="middle" font-size="300" textLength="820" lengthAdjust="spacingAndGlyphs">MORNING</text>
    <text class="title-word" x="600" y="640" text-anchor="middle" font-size="300" textLength="900" lengthAdjust="spacingAndGlyphs">LANTERNS</text>
    <text class="title-word" x="600" y="960" text-anchor="middle" font-size="320" textLength="640" lengthAdjust="spacingAndGlyphs">HILLS</text>
    <text class="title-accent" x="600" y="720" text-anchor="middle" font-size="170" transform="rotate(-9 600 690)">Over</text>
  </g>
</svg>
</body>
</html>
```